Communication and Marketing agency needs a new presentation card

We are a group of communication and marketing agencies specialized in companies that are in the logistics and industrial sector. The head agency is VELUNEX Grupo and the group consists of 4 agencies: VELUNEX Media, VELUNEX Digital, VELUNEX Research and PlanoDeImagenes. We hace 4 offices in Spain (Madrid, Barcelona, Valencia and Murcia). We are looking for a clean and attractive design that transmits our experience, brand presence in the market and knowledge to those who receive the card.It has to maintain the colors of the logo that is attached.
logistics and industrial sector
Marketing department
Clean and attractive design

```html
<!DOCTYPE html>
<html lang="en">
<head>
<meta charset="utf-8">
<title>VELUNEX Grupo – Business Card</title>
<link rel="stylesheet" href="https://fonts.googleapis.com/css2?family=Montserrat:wght@400;500;700&display=swap">
<style>
  :root {
    --red: #c8102e;
    --ink: #3a3a3c;
    --grey: #58585b;
    --card: #fbfbfc;
    --backdrop: #e6e7ea;
  }
  * { margin: 0; padding: 0; box-sizing: border-box; }
  html, body {
    width: 1200px; height: 923px; overflow: hidden;
    background: var(--backdrop);
    font-family: "Montserrat", sans-serif;
  }
  .card {
    position: absolute; left: 75px; top: 161px;
    width: 1050px; height: 600px;
    background: var(--card);
    box-shadow: 0 10px 30px rgba(0,0,0,0.12);
  }
  .person { position: absolute; left: 70px; top: 62px; }
  .person__name {
    color: var(--red); font-weight: 700; font-size: 40px;
    letter-spacing: 0.5px; line-height: 1;
  }
  .person__title {
    color: var(--ink); font-weight: 500; font-size: 29px;
    margin-top: 2px;
  }
  .person__rule {
    width: 50px; height: 5px; background: var(--red); margin-top: 10px;
  }
  .contact {
    position: absolute; left: 70px; top: 330px;
    color: var(--ink); font-size: 25px; line-height: 36px;
  }
  .contact__line { display: flex; align-items: center; gap: 8px; }
  .contact__icon { width: 22px; height: 22px; flex: none; }
  .brand-main {
    position: absolute; right: 80px; top: 190px; text-align: right;
  }
  .brand-main__name {
    color: var(--red); font-weight: 500; font-size: 96px;
    letter-spacing: 2px; line-height: 1;
  }
  .brand-main__sub {
    color: var(--grey); font-weight: 500; font-size: 52px; line-height: 1.1;
  }
  .agencies {
    position: absolute; right: 80px; top: 390px;
    display: flex; flex-direction: column; align-items: flex-end; gap: 10px;
  }
  .agency { font-weight: 500; font-size: 26px; line-height: 1.2; color: var(--ink); }
  .agency--red { color: var(--red); }
</style>
</head>
<body>
  <div class="card">
    <div class="person">
      <div class="person__name">DARIEN HOLT</div>
      <div class="person__title">Managing Director</div>
      <div class="person__rule"></div>
    </div>

    <div class="contact">
      <div class="contact__line">Suite 214 Calle Norte</div>
      <div class="contact__line">Madrid, 28015, Spain</div>
      <div class="contact__line">
        <svg class="contact__icon" viewBox="0 0 24 24" fill="none" stroke="#c8102e" stroke-width="1.6">
          <circle cx="12" cy="12" r="10.5"/>
          <path d="M8.5 7l2 2.2-1.2 1.5c.8 1.6 2 2.8 3.6 3.6l1.5-1.2 2.2 2-1.4 1.6c-3.6-.6-6.7-3.7-7.3-7.3z"/>
        </svg>
        +34 (0)9.14.27.63.58
      </div>
      <div class="contact__line">
        <svg class="contact__icon" viewBox="0 0 24 24" fill="none" stroke="#c8102e" stroke-width="1.6">
          <circle cx="12" cy="12" r="10.5"/>
          <rect x="6.5" y="8" width="11" height="8"/>
          <path d="M6.5 8l5.5 4.5L17.5 8"/>
        </svg>
        hola@velunexgrupo.es
      </div>
      <div class="contact__line">
        <svg class="contact__icon" viewBox="0 0 24 24" fill="none" stroke="#c8102e" stroke-width="1.6">
          <circle cx="12" cy="12" r="10.5"/>
          <ellipse cx="12" cy="12" rx="4" ry="7"/>
          <path d="M5 12h14"/>
        </svg>
        www.velunexgrupo.es
      </div>
    </div>

    <div class="brand-main">
      <div class="brand-main__name">VELUNEX</div>
      <div class="brand-main__sub">Grupo</div>
    </div>

    <div class="agencies">
      <div class="agency">VELUNEX Digital</div>
      <div class="agency">VELUNEX Research</div>
      <div class="agency agency--red">VELUNEX Media</div>
      <div class="agency agency--red">PlanoDeImagenes</div>
    </div>
  </div>
</body>
</html>
```